Brindle Gardenworks Business Card

An eye catching, yet simple business card that includes;

1. our logo
2. office phone - 5127730194
3. email - brindlegardenworks@mailnest.example
4. website - www.brindlegardenworks.example
5. instagram - @brindlegardenworksrvt

```html
<!DOCTYPE html>
<html lang="en">
<head>
<meta charset="utf-8">
<title>Brindle Gardenworks – Business Card</title>
<link rel="stylesheet" href="https://fonts.googleapis.com/css2?family=Montserrat:wght@500;700;800&family=Lato:wght@400&display=swap">
<style>
  :root {
    --bg: #2b2d31;
    --card-white: #ffffff;
    --card-black: #1c1614;
    --brown: #b0672a;
    --ink: #141111;
    --grey: #6b6b6b;
    --rule: #9a9a9a;
  }
  * { margin: 0; padding: 0; box-sizing: border-box; }
  html, body { width: 1200px; height: 952px; overflow: hidden; }
  body {
    background: var(--bg);
    display: flex;
    flex-direction: column;
    align-items: center;
    justify-content: center;
    gap: 40px;
    font-family: "Lato", sans-serif;
  }
  .card {
    position: relative;
    width: 680px;
    height: 388px;
    box-shadow: 0 14px 30px rgba(0,0,0,.45);
  }
  .card--front { background: var(--card-white); }
  .card--back {
    background: var(--card-black);
    display: flex;
    align-items: center;
    justify-content: center;
  }

  .brand {
    display: flex;
    align-items: center;
    gap: 12px;
    font-family: "Montserrat", sans-serif;
    font-weight: 800;
    color: var(--brown);
    text-transform: uppercase;
    line-height: 1.02;
    letter-spacing: .02em;
  }
  .brand__dot {
    flex: none;
    border-radius: 50%;
    background: var(--brown);
  }
  .card--front .brand {
    position: absolute;
    left: 62px;
    top: 92px;
    font-size: 30px;
  }
  .card--front .brand__dot { width: 34px; height: 34px; }
  .card--back .brand { font-size: 44px; gap: 18px; }
  .card--back .brand__dot { width: 50px; height: 50px; }

  .base-rule {
    position: absolute;
    left: 0; top: 0;
  }

  .contact {
    position: absolute;
    left: 392px;
    top: 96px;
    width: 270px;
  }
  .contact__name {
    font-family: "Montserrat", sans-serif;
    font-size: 19px;
    letter-spacing: .01em;
    white-space: nowrap;
  }
  .contact__given { color: var(--brown); font-weight: 500; }
  .contact__family { color: var(--ink); font-weight: 800; }
  .contact__title {
    font-size: 15px;
    color: var(--grey);
    margin-top: 2px;
  }
  .contact__divider {
    width: 48px;
    height: 1px;
    background: var(--rule);
    margin: 8px 0 14px;
  }
  .contact__list { list-style: none; }
  .contact__item {
    display: flex;
    align-items: center;
    gap: 9px;
    font-size: 12.5px;
    color: var(--grey);
    height: 26px;
    white-space: nowrap;
  }
  .contact__icon { flex: none; width: 17px; height: 17px; }
</style>
</head>
<body>

  <section class="card card--front" aria-label="Business card front">
    <div class="brand">
      <span class="brand__dot"></span>
      <span>Brindle<br>Gardenworks</span>
    </div>

    <svg class="base-rule" width="680" height="388" viewBox="0 0 680 388" aria-hidden="true">
      <line x1="38" y1="312" x2="322" y2="312" stroke="var(--brown)" stroke-width="3"/>
      <polygon points="316,318 680,318 680,328 326,328" fill="var(--ink)"/>
    </svg>

    <div class="contact">
      <p class="contact__name"><span class="contact__given">MARTIN J. </span><span class="contact__family">HOLLOWAY</span></p>
      <p class="contact__title">Managing Director</p>
      <div class="contact__divider"></div>
      <ul class="contact__list">
        <li class="contact__item">
          <svg class="contact__icon" viewBox="0 0 18 18" aria-hidden="true">
            <rect width="18" height="18" rx="3" fill="var(--brown)"/>
            <path d="M6 4.5c.6 0 1.6 2 1.6 2.4s-.9.9-.9 1.3c.3 1.1 1.6 2.4 2.7 2.7.4 0 .9-.9 1.3-.9s2.4 1 2.4 1.6c0 .8-1 1.9-1.9 1.9C8.2 13.5 4.5 9.8 4.5 6.4c0-.9 1.1-1.9 1.5-1.9z" fill="#fff"/>
          </svg>
          <span>5127730194</span>
        </li>
        <li class="contact__item">
          <svg class="contact__icon" viewBox="0 0 18 18" aria-hidden="true">
            <rect width="18" height="18" rx="3" fill="var(--brown)"/>
            <rect x="4" y="5.5" width="10" height="7" fill="none" stroke="#fff" stroke-width="1.2"/>
            <path d="M4 5.5l5 4 5-4" fill="none" stroke="#fff" stroke-width="1.2"/>
          </svg>
          <span>brindlegardenworks@mailnest.example</span>
        </li>
        <li class="contact__item">
          <svg class="contact__icon" viewBox="0 0 18 18" aria-hidden="true">
            <rect width="18" height="18" rx="3" fill="var(--brown)"/>
            <path d="M5 4l8 4.5-3.5 1L8 13z" fill="#fff"/>
          </svg>
          <span>www.brindlegardenworks.example</span>
        </li>
        <li class="contact__item">
          <svg class="contact__icon" viewBox="0 0 18 18" aria-hidden="true">
            <rect width="18" height="18" rx="3" fill="var(--brown)"/>
            <rect x="4.5" y="4.5" width="9" height="9" rx="2" fill="none" stroke="#fff" stroke-width="1.2"/>
          </svg>
          <span>@brindlegardenworksrvt</span>
        </li>
      </ul>
    </div>
  </section>

  <section class="card card--back" aria-label="Business card back">
    <div class="brand">
      <span class="brand__dot"></span>
      <span>Brindle<br>Gardenworks</span>
    </div>
  </section>

</body>
</html>
```